We are a new company with 2 divisions a medical research and medical product sales. We need a company logo and Business Cards. The design files need to be provided to us in Adobe Photoshop CS 5.1.

Target Market(s)

Medical Community

Industry/Entity Type

Medical

Contact Information for Business Card

Company Name - Harborline Biomedical LLC
Company Address 4150 SW 17th Ave Suite 8, Gainesville Fl 32611

Requirements
Must have
• The design files need to be provided to us in Adobe Photoshop CS 5.1.

```html
<!DOCTYPE html>
<html lang="en">
<head>
<meta charset="utf-8">
<title>Harborline Biomedical LLC – Business Card</title>
<link href="https://fonts.googleapis.com/css2?family=Open+Sans:wght@400&family=Quicksand:wght@400&display=swap" rel="stylesheet">
<style>
  :root {
    --page-bg: #2b2b2d;
    --card-white: #f4f4f4;
    --card-white-edge: #e2e2e2;
    --coral: #e05d5d;
    --coral-light: #ea6a68;
    --leaf: #9fc04d;
    --brand-blue: #1f5fa6;
    --rule: rgba(255,255,255,0.3);
    --ink-light: #ffffff;
  }
  html, body {
    margin: 0;
    width: 1200px;
    height: 800px;
    overflow: hidden;
    background: var(--page-bg);
  }
  .stage {
    width: 1200px;
    height: 800px;
    display: flex;
    align-items: center;
    justify-content: center;
  }
  .business-card {
    position: relative;
    width: 1000px;
    height: 580px;
    box-shadow: 0 18px 40px rgba(0,0,0,0.45);
  }
  .card-art {
    position: absolute;
    inset: 0;
  }
  .brand {
    position: absolute;
    left: 60px;
    top: 392px;
    display: flex;
    align-items: center;
    gap: 14px;
  }
  .brand-dot {
    width: 20px;
    height: 20px;
    border-radius: 50%;
    background: var(--brand-blue);
  }
  .brand-name {
    font-family: "Open Sans", Verdana, sans-serif;
    font-weight: 400;
    font-size: 34px;
    line-height: 46px;
    color: var(--brand-blue);
    letter-spacing: 0.5px;
    margin: 0;
    white-space: nowrap;
  }
  .contact-line {
    position: absolute;
    font-family: "Quicksand", sans-serif;
    font-weight: 400;
    color: var(--ink-light);
    margin: 0;
    white-space: nowrap;
  }
  .contact-address {
    left: 640px;
    top: 192px;
    font-size: 23px;
    line-height: 31px;
  }
  .contact-address span { display: block; }
  .contact-address span + span { padding-left: 22px; }
  .contact-phone {
    left: 680px;
    top: 286px;
    font-size: 27px;
    line-height: 34px;
    letter-spacing: 1px;
  }
</style>
</head>
<body>
<main class="stage">
  <article class="business-card">
    <svg class="card-art" viewBox="0 0 1000 580" width="1000" height="580" aria-hidden="true">
      <defs>
        <radialGradient id="whiteGlow" cx="0.55" cy="0.55" r="0.7">
          <stop offset="0" stop-color="var(--card-white)"/>
          <stop offset="1" stop-color="var(--card-white-edge)"/>
        </radialGradient>
        <linearGradient id="coralShade" x1="0" y1="1" x2="1" y2="0">
          <stop offset="0" stop-color="var(--coral-light)"/>
          <stop offset="1" stop-color="var(--coral)"/>
        </linearGradient>
      </defs>
      <rect class="panel-white" width="1000" height="580" fill="url(#whiteGlow)"/>
      <polygon class="panel-coral" points="420,0 1000,0 1000,290 690,494" fill="url(#coralShade)"/>
      <polygon class="panel-leaf" points="560,580 1000,290 1000,580" fill="var(--leaf)"/>

      <line class="contact-rule" x1="622" y1="264" x2="980" y2="264" stroke="var(--rule)" stroke-width="1.5"/>
      <line class="contact-rule" x1="662" y1="338" x2="915" y2="338" stroke="var(--rule)" stroke-width="1.5"/>

      <g class="icon-tab icon-pin">
        <rect x="560" y="200" width="62" height="54" fill="var(--leaf)"/>
        <path d="M591 215 a9 9 0 0 1 9 9 c0 7 -9 16 -9 16 s-9 -9 -9 -16 a9 9 0 0 1 9 -9z" fill="#fff"/>
        <circle cx="591" cy="224" r="3.2" fill="var(--leaf)"/>
      </g>
      <g class="icon-tab icon-phone">
        <rect x="600" y="276" width="62" height="54" fill="var(--leaf)"/>
        <path d="M622 291 l5 -2 l4 8 l-3 3 c2 4 5 7 9 9 l3 -3 l8 4 l-2 5 c-12 1 -25 -12 -24 -24z" fill="#fff"/>
      </g>
    </svg>

    <div class="brand">
      <span class="brand-dot"></span>
      <h1 class="brand-name">Harborline Biomedical LLC</h1>
    </div>

    <p class="contact-line contact-address">
      <span>4150 SW 17th Ave Suite 8,</span>
      <span>Gainesville Fl 32611</span>
    </p>
    <p class="contact-line contact-phone">555 201 480</p>
  </article>
</main>
</body>
</html>
```